Enterprise Business Application

We need a two sided brochure for our new application named The PIVOT Metrics™. This cloud-based application is designed to help clients assess, track and coach employee performance. Our patent pending algorithm allows users to prioritize attributes for competencies classified as knowledge, skill and ability. We enhance the traditional process by standardizing coaching and reducing the amount of time required to coach performance.

We would like the brochure layout and them to compliment the enhancements we are making to our website.

Target Market(s)

Performance Managers

Industry/Entity Type

Business Software

Font styles to use
Sans Serif

Colors
9bcb3c
abd037
cadf82
eaf2ce
ffc214
fece3e
0792cd
33a6d7
f37122

Requirements
Must have
• incorporate our logo and brand colors, clean UX design,
Should not have
• Exaggerated overly happy Stock Photos

```html
<!DOCTYPE html>
<html lang="en">
<head>
<meta charset="utf-8">
<title>The PIVOT Metrics™ – Brochure</title>
<link href="https://fonts.googleapis.com/css2?family=Oswald:wght@400;500&family=Rajdhani:wght@500;600;700&display=swap" rel="stylesheet">
<style>
  :root{
    --page-bg:#e9ecef;
    --navy:#0b1a33;
    --deep-blue:#0a3f86;
    --brand-blue:#0792cd;
    --sky-blue:#33a6d7;
    --bright-blue:#1a78c8;
    --lime:#c0dc2f;
    --lime-dark:#a9c92a;
    --white:#ffffff;
    --ink:#0d1b2a;
  }
  *{box-sizing:border-box;margin:0;padding:0}
  html,body{width:1200px;height:994px;overflow:hidden;background:var(--page-bg)}
  body{position:relative;font-family:"Rajdhani",sans-serif;color:var(--white)}
  .brochure{position:absolute;left:0;top:74px;width:1348px;height:951px;transform:scale(.8902);transform-origin:0 0;overflow:hidden}

  /* ---------- back panel ---------- */
  .back-panel{position:absolute;left:0;top:0;width:674px;height:951px;
    background:radial-gradient(ellipse at 60% 55%,#2f9fe0 0%,#1268c0 45%,#0a3f86 80%,#08306d 100%)}
  .sky-scene{position:absolute;left:0;top:740px;width:1348px;height:211px;
    background:linear-gradient(180deg,rgba(51,166,215,0) 0%,#3aa5e2 40%,#7cc4ee 100%)}
  .section-title{font-weight:700;font-size:31px;letter-spacing:1.5px;text-align:center;position:absolute;left:0;width:674px}
  .about-title{top:32px}
  .about-copy{position:absolute;left:39px;top:88px;width:598px;font-size:12.6px;font-weight:500;line-height:16.4px;letter-spacing:.3px}
  .about-copy p{margin-bottom:10px}
  .trial-title{top:282px}
  .field-label{position:absolute;font-size:15px;font-weight:600;letter-spacing:.5px}
  .field-box{position:absolute;height:23px;border:1.5px solid rgba(255,255,255,.85);border-radius:2px;background:rgba(255,255,255,.05)}
  .help-label{position:absolute;left:0;width:662px;text-align:center;top:462px;font-size:15px;font-weight:600;letter-spacing:.5px}
  .help-box{position:absolute;left:145px;top:495px;width:390px;height:100px;border:1.5px solid rgba(255,255,255,.85)}
  .contact-band{position:absolute;left:0;top:617px;width:484px;height:132px;background:var(--navy);text-align:center;padding-top:24px}
  .contact-title{font-weight:700;font-size:30px;letter-spacing:1.5px;line-height:34px}
  .contact-line{font-size:15px;font-weight:600;letter-spacing:.6px;line-height:24px}
  .web-address{position:absolute;left:0;width:690px;text-align:center;top:825px;font-size:19px;font-weight:600;color:var(--ink);letter-spacing:.8px}

  /* ---------- front panel ---------- */
  .front-panel{position:absolute;left:674px;top:0;width:674px;height:951px;
    background:linear-gradient(180deg,#1b6fc3 0%,#1463b8 60%,#0f56a8 100%)}
  .fold-strip{position:absolute;left:0;top:0;width:123px;height:500px;background:linear-gradient(180deg,#0d3f88,#1f7fd0)}
  .hero-photo{position:absolute;left:123px;top:0;width:551px;height:500px;
    background:radial-gradient(ellipse at 75% 55%,#4a5f7c 0%,#2a3a55 40%,#16233a 100%)}
  .hero-rules{position:absolute;left:123px;top:464px;width:551px;height:30px}
  .brand-lockup{position:absolute;left:165px;top:42px;display:flex;align-items:center;gap:12px}
  .brand-dot{width:30px;height:30px;border-radius:50%;background:var(--sky-blue)}
  .brand-name{font-weight:700;font-size:44px;letter-spacing:1px;color:var(--white);line-height:1}
  .headline{position:absolute;left:0;width:674px;top:516px;text-align:center;font-family:"Oswald",sans-serif;line-height:1}
  .headline-main{font-weight:500;font-size:60px;letter-spacing:.5px;display:block}
  .headline-sub{font-weight:400;font-size:40px;letter-spacing:4px;display:block;margin-top:4px}
  .lime-band{position:absolute;left:484px;top:638px;width:826px;height:136px;background:var(--lime);border-top-right-radius:42px}
  .lime-band .fold-shade{position:absolute;left:0;top:0;width:190px;height:136px;background:var(--lime-dark)}
  .lime-band .corner-flap{position:absolute;left:0;top:-20px}
  .lime-copy{position:absolute;left:190px;width:636px;top:12px;text-align:center;color:var(--ink);font-size:16px;font-weight:600;letter-spacing:.6px;line-height:19px}
  .trial-button{position:absolute;left:412px;top:62px;width:176px;height:52px;border-radius:26px;
    background:linear-gradient(180deg,#1d6ad0,#0a3f8e);box-shadow:0 0 0 5px rgba(10,63,142,.15);display:flex;align-items:center;padding-left:30px}
  .trial-button .cta-text{line-height:17px}
  .trial-button .cta-main{font-weight:700;font-size:18px;letter-spacing:1px;display:block}
  .trial-button .cta-sub{font-weight:500;font-size:14px;letter-spacing:1px;display:block;color:#cfe3f7}
  .trial-button svg{position:absolute;right:10px;top:9px}
  .welcome-box{position:absolute;left:54px;top:774px;width:553px;height:177px;
    background:linear-gradient(180deg,#0d54b4 0%,#1b7fd6 70%,#62b7ea 100%);text-align:center}
  .welcome-title{font-weight:600;font-size:22px;letter-spacing:2px;margin-top:16px}
  .welcome-copy{font-size:14px;font-weight:600;letter-spacing:.5px;line-height:17.5px;margin:8px 26px 0}
  .welcome-rules{position:absolute;left:0;bottom:6px;width:553px;height:22px}
</style>
</head>
<body>
<main class="brochure">

  <section class="back-panel">
    <h2 class="section-title about-title">ABOUT US:</h2>
    <div class="about-copy">
      <p>Our story is built on the desire to contribute to the art and science of leadership through effective and efficient performance management.</p>
      <p>Today’s business leaders are inundated with responsibilities, many of which are time consuming and limit the ability to focus on a critical component of success–employee development. Studies have shown employees who don’t feel they are being developed and challenged are less productive and less loyal than those who receive regular feedback and coaching.</p>
      <p>We have been passionate about employee performance and development for over 20 years as sales leaders and educators who experienced inefficiencies and ineffectiveness first hand. We are excited to change the way performance is managed, today and in the future.</p>
    </div>

    <h2 class="section-title trial-title">TRIAL REGISTRATION:</h2>
    <span class="field-label" style="left:28px;top:342px">First Name</span>
    <span class="field-box" style="left:119px;top:342px;width:211px"></span>
    <span class="field-label" style="left:343px;top:342px">Last Name</span>
    <span class="field-box" style="left:434px;top:342px;width:211px"></span>
    <span class="field-label" style="left:28px;top:381px">Company Name</span>
    <span class="field-box" style="left:153px;top:380px;width:212px"></span>
    <span class="field-label" style="left:386px;top:381px">Title</span>
    <span class="field-box" style="left:433px;top:380px;width:212px"></span>
    <span class="field-label" style="left:28px;top:422px">Email Address</span>
    <span class="field-box" style="left:143px;top:421px;width:179px"></span>
    <span class="field-label" style="left:332px;top:422px">Telephone Number</span>
    <span class="field-box" style="left:475px;top:421px;width:170px"></span>
    <span class="help-label">How Can We Help You?</span>
    <span class="help-box"></span>

    <div class="contact-band">
      <h2 class="contact-title">CONTACT US :</h2>
      <p class="contact-line">Email Us: jordan@thepivotmetrics.com</p>
      <p class="contact-line">Call Us: 1.800.555.PIVT (7488)</p>
    </div>
  </section>

  <div class="sky-scene" role="img" aria-label="Soft blue sky with white clouds along the bottom of the brochure"></div>
  <p class="web-address">www.pivotmetrics-app.com</p>

  <section class="front-panel">
    <div class="fold-strip"></div>
    <div class="hero-photo" role="img" aria-label="Photo of a hand drawing a rising performance curve on a dark glass board"></div>
    <svg class="hero-rules" viewBox="0 0 551 30" aria-hidden="true">
      <rect x="0" y="2" width="551" height="3" fill="#1f7fd0"/>
      <rect x="0" y="11" width="551" height="2" fill="#1f7fd0"/>
      <rect x="0" y="19" width="551" height="2" fill="#1f7fd0"/>
    </svg>
    <div class="brand-lockup">
      <span class="brand-dot"></span>
      <span class="brand-name">The PIVOT Metrics</span>
    </div>

    <h1 class="headline">
      <span class="headline-main">EMPLOYEE PERFORMANCE</span>
      <span class="headline-sub">AT YOUR FINGERTIPS</span>
    </h1>

    <div class="welcome-box">
      <h3 class="welcome-title">WELCOME TO THE PIVOT METRICS™</h3>
      <p class="welcome-copy">With The PIVOT Metrics, you can now get real-time results for employee development and performance in key competency areas. Our trending and analysis features help you manage your business with forward-thinking insights with data such as progress over time.</p>
      <svg class="welcome-rules" viewBox="0 0 553 22" aria-hidden="true">
        <rect x="0" y="0" width="553" height="2" fill="#d6ecfb" opacity=".8"/>
        <rect x="0" y="7" width="553" height="2" fill="#d6ecfb" opacity=".8"/>
        <rect x="0" y="14" width="553" height="2" fill="#d6ecfb" opacity=".8"/>
      </svg>
    </div>
  </section>

  <div class="lime-band">
    <div class="fold-shade"></div>
    <svg class="corner-flap" width="44" height="20" viewBox="0 0 44 20" aria-hidden="true">
      <polygon points="0,20 44,0 44,20" fill="#eaf2ce"/>
    </svg>
    <p class="lime-copy">The PIVOT Metrics™ is a web-based tool designed to help you<br>measure employee performance efficiently and effectively.</p>
    <a class="trial-button">
      <span class="cta-text"><span class="cta-main">TRY PIVOT</span><span class="cta-sub">30 Day Trial</span></span>
      <svg width="34" height="34" viewBox="0 0 34 34" aria-hidden="true">
        <circle cx="17" cy="17" r="15" fill="#0a3f8e" stroke="#33a6d7" stroke-width="2.5"/>
        <polyline points="14,10 21,17 14,24" fill="none" stroke="#ffffff" stroke-width="3" stroke-linecap="round" stroke-linejoin="round"/>
      </svg>
    </a>
  </div>

</main>
</body>
</html>
```